Beer bottle label / Tap badge

What: Graphics to be used on both a beer tap badge and a beer bottle label
Requirements:
• Represent a differentiated quality product
• Include brewery name and logo for brand recognition
• Include and represent the Name “Idle Tide”
• Include the beer style “American Cream Ale”
• A format that can be used both in a circular tap badge and a square / rectangular bottle label
At Drifting Reed Brewing Co. we design and brew quality beers across a range of styles. We use traditional ingredients and techniques to produce brews for you that are bursting with flavor and easy to drink. Our passion and commitment to excellence are captured in every bottle. Give them a try and see what we mean.
Idle Tide
American Cream Ale
An easy drinking session beer that won’t make you work to enjoy it. This is crafted to be smooth with a modicum of honey toasted oats and a yeast strain that leaves a fruity, very light, soft balanced palate. Perfectly hopped for a balanced experience this beer is made for you.
Updates
Thanks to everyone who submitted a design. My apologies for not providing any feedback over the past few days since we took a short break over Christmas. We've extended the deadline by a few days and we'll be in touch shortly.
Industry/Entity Type
Brewery
Requirements
Must have
- - Include brewery name and logo for brand recognition
- Include and represent the Name “Idle Tide”
- Include the beer style “American Cream Ale”
- include volume (330ml) and % alcohol (4.5% alcohol)
Nice to have
- Idle Tide is a very drinkable, smooth and easy beer that is perfect for a sunny lazy afternoon. We would like the graphic to represent the beer. So, perhaps a friendly (smiling) skeleton on a hammock or on the beach enjoying life .....

```html
<!DOCTYPE html>
<html lang="en">
<head>
<meta charset="utf-8">
<title>Idle Tide – American Cream Ale label</title>
<link rel="stylesheet" href="https://fonts.googleapis.com/css2?family=Pinyon+Script&family=Arimo:wght@400;700&display=swap">
<style>
  :root {
    --page: #ffffff;
    --gold-light: #e2c48a;
    --gold: #b08a4e;
    --gold-dark: #7d5f2e;
    --frame-dark: #3b3a38;
    --cream: #e7e5dc;
    --cream-light: #f4f3ee;
    --script: #7a6649;
    --ink: #1e1e1e;
    --muted: #a99d83;
  }
  html, body {
    margin: 0;
    width: 1200px;
    height: 900px;
    overflow: hidden;
    background: var(--page);
  }
  .canvas { position: relative; width: 1200px; height: 900px; }
  .label { position: absolute; left: 0; top: 0; }
  .beer-name { font-family: "Pinyon Script", cursive; font-size: 74px; fill: var(--script); }
  .beer-style { font-family: "Arimo", Arial, sans-serif; font-weight: 700; font-size: 21px; fill: var(--ink); letter-spacing: 0.5px; }
  .spec { font-family: "Arimo", Arial, sans-serif; font-size: 15px; fill: var(--muted); }
  .brewery-name { font-family: "Arimo", Arial, sans-serif; font-weight: 700; font-size: 17px; fill: var(--ink); }
</style>
</head>
<body>
<main class="canvas">
  <svg class="label" width="1200" height="900" viewBox="0 0 1200 900" aria-label="Idle Tide American Cream Ale label">
    <defs>
      <linearGradient id="goldFrame" x1="0" y1="0" x2="1" y2="1">
        <stop offset="0" stop-color="var(--gold-dark)"/>
        <stop offset="0.35" stop-color="var(--gold-light)"/>
        <stop offset="0.65" stop-color="var(--gold)"/>
        <stop offset="1" stop-color="var(--gold-dark)"/>
      </linearGradient>
      <radialGradient id="creamPanel" cx="0.5" cy="0.5" r="0.7">
        <stop offset="0" stop-color="var(--cream-light)"/>
        <stop offset="1" stop-color="var(--cream)"/>
      </radialGradient>
    </defs>

    <!-- upper crest -->
    <g class="crest-top">
      <path d="M232 345 L232 262 Q262 262 268 236 C300 220 330 180 345 150 Q393 118 441 150 C456 180 486 220 518 236 Q524 262 554 262 L554 345 Z"
            fill="url(#creamPanel)" stroke="url(#goldFrame)" stroke-width="34" stroke-linejoin="round"/>
      <path d="M232 345 L232 262 Q262 262 268 236 C300 220 330 180 345 150 Q393 118 441 150 C456 180 486 220 518 236 Q524 262 554 262 L554 345 Z"
            fill="none" stroke="var(--frame-dark)" stroke-width="18" stroke-linejoin="round"/>
      <path d="M232 345 L232 262 Q262 262 268 236 C300 220 330 180 345 150 Q393 118 441 150 C456 180 486 220 518 236 Q524 262 554 262 L554 345 Z"
            fill="url(#creamPanel)" stroke="url(#goldFrame)" stroke-width="6" stroke-linejoin="round"/>
    </g>

    <!-- lower crest -->
    <g class="crest-bottom">
      <path d="M232 570 L232 652 Q262 652 268 678 C300 702 330 740 345 764 Q393 796 441 764 C456 740 486 702 518 678 Q524 652 554 652 L554 570 Z"
            fill="url(#creamPanel)" stroke="url(#goldFrame)" stroke-width="34" stroke-linejoin="round"/>
      <path d="M232 570 L232 652 Q262 652 268 678 C300 702 330 740 345 764 Q393 796 441 764 C456 740 486 702 518 678 Q524 652 554 652 L554 570 Z"
            fill="none" stroke="var(--frame-dark)" stroke-width="18" stroke-linejoin="round"/>
      <path d="M232 570 L232 652 Q262 652 268 678 C300 702 330 740 345 764 Q393 796 441 764 C456 740 486 702 518 678 Q524 652 554 652 L554 570 Z"
            fill="url(#creamPanel)" stroke="url(#goldFrame)" stroke-width="6" stroke-linejoin="round"/>
    </g>

    <!-- mascot area -->
    <rect class="mascot" x="318" y="176" width="132" height="158" rx="6" fill="#cdb98c" opacity="0.75"
          role="img" aria-label="Illustration of a relaxed skeleton sitting with one knee raised"/>

    <!-- central name band -->
    <g class="name-band">
      <rect x="163" y="336" width="460" height="244" rx="22" fill="url(#goldFrame)"/>
      <rect x="178" y="349" width="430" height="218" rx="12" fill="url(#creamPanel)" stroke="var(--gold)" stroke-width="2"/>
      <text class="beer-name" x="393" y="445" text-anchor="middle">Idle Tide</text>
      <line x1="203" y1="460" x2="583" y2="460" stroke="var(--script)" stroke-width="2"/>
      <text class="beer-style" x="393" y="497" text-anchor="middle">AMERICAN CREAM ALE</text>
      <text class="spec" x="190" y="552">4.5 % de alcohol</text>
      <text class="spec" x="596" y="552" text-anchor="end">Volumen 330 ml</text>
    </g>

    <!-- brewery seal -->
    <g class="brewery-seal">
      <circle cx="393" cy="578" r="74" fill="url(#goldFrame)"/>
      <circle cx="393" cy="578" r="64" fill="#ffffff"/>
      <text class="brewery-name" x="393" y="558" text-anchor="middle">Drifting</text>
      <text class="brewery-name" x="393" y="580" text-anchor="middle">Reed</text>
      <text class="brewery-name" x="393" y="602" text-anchor="middle">Brewing Co.</text>
    </g>
  </svg>
</main>
</body>
</html>
```